Powerpoint Template with Pitch Slides, a logo, color palette and a few business diagrams

1) Powerpoint Template with Pitch Slides that are drafted in attached document
2) Color palette for Powerpoint Template. Think a blend between Bold and professional business
3) A Logo for Quilmo Enterprises (i like the icon that I attached)
4) A Quilmo Icon likely pulled from the logo
5) A few business diagrams like the ones attached. Dovenhulm, Lifecyle.

Industry/Entity Type

Applications, Finance

Font styles to use
Other font styles liked:
• Helvetica

```html
<!DOCTYPE html>
<html lang="en">
<head>
<meta charset="utf-8">
<title>Quilmo Enterprises – Pitch Template</title>
<link href="https://fonts.googleapis.com/css2?family=Arimo:wght@400;700&display=swap" rel="stylesheet">
<style>
  :root{
    --page:#7d7f82;
    --orange:#e9a635;
    --orange-deep:#e39a2c;
    --yellow:#f5e64c;
    --ink:#111111;
    --text:#4a4a4a;
    --paper:#faf8f5;
    --white:#ffffff;
  }
  *{margin:0;padding:0;box-sizing:border-box}
  html,body{width:1200px;height:4112px;overflow:hidden}
  body{background:var(--page);font-family:"Arimo",Helvetica,Arial,sans-serif;color:var(--ink);position:relative}
  .slide{position:absolute;left:51px;width:1097px;height:616px;overflow:hidden}
  .slide--brand{background:radial-gradient(ellipse 60% 70% at 50% 48%,var(--yellow) 0%,#f1c545 45%,var(--orange) 100%)}
  .slide--content{background:linear-gradient(135deg,var(--paper) 0%,#f4f1ec 100%)}
  .page-no{position:absolute;left:1047px;top:567px;width:29px;height:29px;border-radius:50%;background:var(--ink);color:var(--white);font-size:11px;font-weight:700;display:flex;align-items:center;justify-content:center}

  /* brand lockup */
  .lockup-mark{position:absolute;width:124px;height:124px;border-radius:50%;background:var(--ink)}
  .lockup-name{position:absolute;font-weight:700;font-size:47px;line-height:51px;letter-spacing:1px;color:var(--ink)}
  .cover-title{position:absolute;left:0;width:100%;text-align:center;font-weight:700;font-size:48px;color:var(--ink)}
  .cover-tagline{position:absolute;left:0;width:100%;text-align:center;font-weight:700;font-size:22px;color:var(--ink)}

  /* content slide header */
  .slide-heading{position:absolute;left:34px;top:24px;font-weight:700;font-size:45px;line-height:45px;color:var(--ink)}
  .heading-tab{position:absolute;left:0;top:32px;width:26px;height:30px}
  .footer-brand{position:absolute;left:24px;top:540px;display:flex;align-items:center;gap:12px}
  .footer-brand .dot{width:58px;height:58px;border-radius:50%;background:var(--ink)}
  .footer-brand .name{font-weight:700;font-size:13px;line-height:15px;color:var(--ink)}

  /* team */
  .member{position:absolute;top:165px;width:220px;text-align:center}
  .member .photo{width:118px;height:118px;border-radius:50%;margin:0 auto;background:linear-gradient(160deg,#8a8d92,#3d4047);border:3px solid #fff}
  .member .name{margin-top:20px;font-weight:700;font-size:22px}
  .member .bio{margin-top:8px;font-size:11px;line-height:16px;color:var(--text)}

  /* problem cards */
  .card{position:absolute;width:300px;height:173px;background:var(--white);box-shadow:0 2px 8px rgba(0,0,0,.08)}
  .card .badge{position:absolute;left:0;top:0;width:69px;height:64px;background:var(--orange);border-radius:0 0 40px 0;color:var(--white);font-weight:700;font-size:27px;display:flex;align-items:center;justify-content:center;padding-right:6px}
  .card .title{position:absolute;left:88px;top:16px;font-weight:700;font-size:22px}
  .card .body{position:absolute;left:20px;top:87px;width:270px;font-size:11px;line-height:23px;color:var(--text)}

  /* solution */
  .solution-copy{position:absolute;left:34px;top:106px;width:459px;font-size:13.5px;line-height:28.5px;font-weight:700;color:var(--text);text-align:justify}
  .solution-tree{position:absolute;left:0;top:0}
  .point-label{position:absolute;left:803px;font-weight:700;font-size:22px;transform:translateY(-50%)}

  /* lifecycle */
  .stage-label{position:absolute;top:406px;width:160px;text-align:center;font-weight:700;font-size:14px}
</style>
</head>
<body>

<!-- Cover -->
<section class="slide slide--brand" style="top:51px">
  <div class="lockup-mark" style="left:299px;top:154px"></div>
  <div class="lockup-name" style="left:511px;top:166px">QUILMO<br>ENTERPRISES</div>
  <h1 class="cover-title" style="top:408px">QUILMO ENTERPRISES</h1>
  <p class="cover-tagline" style="top:474px">Consolidate and Drive Your Buisness</p>
  <div class="page-no">01</div>
</section>

<!-- Team -->
<section class="slide slide--content" style="top:728px">
  <svg class="heading-tab" viewBox="0 0 26 30"><polygon points="0,0 17,0 26,15 17,30 0,30" fill="var(--orange)"/></svg>
  <h2 class="slide-heading">OUR TEAM</h2>
  <div class="member" style="left:128px">
    <div class="photo" role="img" aria-label="Portrait photo of Ross Palter"></div>
    <div class="name">Ross Palter</div>
    <p class="bio">Lorem ipsum dolor sit amet, conse ctetur adipiscing elit, sed do eiusmod tempor incididunt ut labore et dolore magna aliqua.</p>
  </div>
  <div class="member" style="left:439px">
    <div class="photo" role="img" aria-label="Portrait photo of Dale Verin"></div>
    <div class="name">Dale Verin</div>
    <p class="bio">Lorem ipsum dolor sit amet, conse ctetur adipiscing elit, sed do eiusmod tempor incididunt ut labore et dolore magna aliqua.</p>
  </div>
  <div class="member" style="left:750px">
    <div class="photo" role="img" aria-label="Portrait photo of Marcus Oduya"></div>
    <div class="name">Marcus Oduya</div>
    <p class="bio">Lorem ipsum dolor sit amet, conse ctetur adipiscing elit, sed do eiusmod tempor incididunt ut labore et dolore magna aliqua.</p>
  </div>
  <div class="footer-brand"><span class="dot"></span><span class="name">QUILMO<br>ENTERPRISES</span></div>
  <div class="page-no">02</div>
</section>

<!-- Problem -->
<section class="slide slide--content" style="top:1403px">
  <svg class="heading-tab" viewBox="0 0 26 30"><polygon points="0,0 17,0 26,15 17,30 0,30" fill="var(--orange)"/></svg>
  <h2 class="slide-heading">OUR PROBLEM</h2>
  <div class="card" style="left:77px;top:105px"><div class="badge">01</div><div class="title">Interpreting</div><p class="body">Lorem ipsum dolor sit amet, consectetur adipi scing elit, sed do eiusmod tempor incididunt ut labore et dolore magna aliqua.</p></div>
  <div class="card" style="left:394px;top:105px"><div class="badge">02</div><div class="title">Dicision Making</div><p class="body">Lorem ipsum dolor sit amet, consectetur adipi scing elit, sed do eiusmod tempor incididunt ut labore et dolore magna aliqua.</p></div>
  <div class="card" style="left:712px;top:105px"><div class="badge">03</div><div class="title">Existing App</div><p class="body">Lorem ipsum dolor sit amet, consectetur adipi scing elit, sed do eiusmod tempor incididunt ut labore et dolore magna aliqua.</p></div>
  <div class="card" style="left:77px;top:305px"><div class="badge">04</div><div class="title">Interfacing</div><p class="body">Lorem ipsum dolor sit amet, consectetur adipi scing elit, sed do eiusmod tempor incididunt ut labore et dolore magna aliqua.</p></div>
  <div class="card" style="left:394px;top:305px"><div class="badge">05</div><div class="title">Data warehouses</div><p class="body">Lorem ipsum dolor sit amet, consectetur adipi scing elit, sed do eiusmod tempor incididunt ut labore et dolore magna aliqua.</p></div>
  <div class="card" style="left:712px;top:305px"><div class="badge">06</div><div class="title">Home Grown</div><p class="body">Lorem ipsum dolor sit amet, consectetur adipi scing elit, sed do eiusmod tempor incididunt ut labore et dolore magna aliqua.</p></div>
  <div class="footer-brand"><span class="dot"></span><span class="name">QUILMO<br>ENTERPRISES</span></div>
  <div class="page-no">03</div>
</section>

<!-- Solution -->
<section class="slide slide--content" style="top:2078px">
  <svg class="heading-tab" viewBox="0 0 26 30"><polygon points="0,0 17,0 26,15 17,30 0,30" fill="var(--orange)"/></svg>
  <h2 class="slide-heading">SOLUTION</h2>
  <p class="solution-copy">Lorem ipsum dolor sit amet, consectetur adipiscing elit, sed do eiusmod tempor incididunt ut labore et dolore magna aliqua. Ut enim ad minim veniam, quis nostrud exercitation ullamco laboris nisi ut aliquip ex ea commodo consequat. Duis aute irure dolor in reprehenderit in voluptate velit esse cillum dolore eu fugiat nulla pariatur. Excepteur sint occaecat cupidatat non proident, sunt in culpa qui officia deserunt mollit anim id est laborum.</p>
  <svg class="solution-tree" width="1097" height="616" viewBox="0 0 1097 616">
    <g fill="none" stroke="var(--ink)" stroke-width="3">
      <polyline points="235,319 235,428 605,428"/>
      <line x1="605" y1="62" x2="605" y2="509"/>
      <line x1="605" y1="62" x2="720" y2="62"/>
      <line x1="605" y1="174" x2="720" y2="174"/>
      <line x1="605" y1="286" x2="720" y2="286"/>
      <line x1="605" y1="397" x2="720" y2="397"/>
      <line x1="605" y1="509" x2="720" y2="509"/>
    </g>
    <g fill="var(--orange)">
      <circle cx="235" cy="319" r="6"/>
      <circle cx="720" cy="62" r="6"/><circle cx="720" cy="174" r="6"/><circle cx="720" cy="286" r="6"/><circle cx="720" cy="397" r="6"/><circle cx="720" cy="509" r="6"/>
    </g>
    <g fill="#f2c53c" stroke="var(--orange)" stroke-width="3">
      <polygon points="760,32 786,47 786,77 760,92 734,77 734,47"/>
      <polygon points="760,144 786,159 786,189 760,204 734,189 734,159"/>
      <polygon points="760,256 786,271 786,301 760,316 734,301 734,271"/>
      <polygon points="760,367 786,382 786,412 760,427 734,412 734,382"/>
      <polygon points="760,479 786,494 786,524 760,539 734,524 734,494"/>
    </g>
    <g font-family="Arimo,Helvetica,Arial,sans-serif" font-weight="700" font-size="18" fill="var(--ink)" text-anchor="middle">
      <text x="760" y="68">01</text><text x="760" y="180">02</text><text x="760" y="292">03</text><text x="760" y="403">04</text><text x="760" y="515">05</text>
    </g>
  </svg>
  <span class="point-label" style="top:62px">Consolidate</span>
  <span class="point-label" style="top:174px">Timely</span>
  <span class="point-label" style="top:286px">Platform</span>
  <span class="point-label" style="top:397px">Confidence</span>
  <span class="point-label" style="top:509px">Promotes</span>
  <div class="footer-brand"><span class="dot"></span><span class="name">QUILMO<br>ENTERPRISES</span></div>
  <div class="page-no">04</div>
</section>

<!-- Lifecycle -->
<section class="slide slide--content" style="top:2753px">
  <svg class="heading-tab" viewBox="0 0 26 30"><polygon points="0,0 17,0 26,15 17,30 0,30" fill="var(--orange)"/></svg>
  <h2 class="slide-heading">LIFECYCLE</h2>
  <svg style="position:absolute;left:0;top:0" width="1097" height="616" viewBox="0 0 1097 616">
    <circle cx="134" cy="283" r="97" fill="var(--yellow)"/>
    <circle cx="342" cy="283" r="97" fill="var(--orange)"/>
    <circle cx="549" cy="283" r="97" fill="var(--yellow)"/>
    <circle cx="757" cy="283" r="97" fill="var(--orange)"/>
    <circle cx="962" cy="283" r="97" fill="var(--yellow)"/>
    <!-- connectors -->
    <g fill="var(--white)"><circle cx="238" cy="289" r="19"/><circle cx="446" cy="289" r="19"/><circle cx="653" cy="289" r="19"/><circle cx="860" cy="289" r="19"/></g>
    <g fill="none" stroke="var(--ink)" stroke-width="2" stroke-linecap="round">
      <path d="M230 293 q8-10 16-2 m0 0 l-1-6 m1 6 l-6 0"/>
      <path d="M438 293 q8-10 16-2 m0 0 l-1-6 m1 6 l-6 0"/>
      <path d="M645 293 q8-10 16-2 m0 0 l-1-6 m1 6 l-6 0"/>
      <path d="M852 293 q8-10 16-2 m0 0 l-1-6 m1 6 l-6 0"/>
    </g>
    <!-- design: pen nib -->
    <g fill="var(--ink)">
      <rect x="104" y="236" width="60" height="8"/>
      <rect x="98" y="232" width="14" height="16"/><rect x="156" y="232" width="14" height="16"/>
      <path d="M134 250 l26 26 l-12 30 h-28 l-12-30z"/>
      <rect x="118" y="310" width="32" height="12"/>
    </g>
    <circle cx="134" cy="282" r="5" fill="var(--yellow)"/>
    <!-- develop: code window -->
    <rect x="292" y="236" width="100" height="92" rx="8" fill="var(--ink)"/>
    <rect x="300" y="258" width="84" height="62" fill="var(--orange)"/>
    <g fill="none" stroke="var(--ink)" stroke-width="6" stroke-linecap="round" stroke-linejoin="round">
      <polyline points="322,277 310,289 322,301"/><polyline points="362,277 374,289 362,301"/><line x1="348" y1="272" x2="336" y2="306"/>
    </g>
    <!-- test: document with tick -->
    <path d="M515 234 h50 l16 16 v68 h-66z" fill="var(--ink)"/>
    <g fill="var(--yellow)"><rect x="527" y="258" width="30" height="6"/><rect x="527" y="272" width="30" height="6"/><rect x="527" y="286" width="20" height="6"/></g>
    <circle cx="573" cy="313" r="20" fill="var(--ink)" stroke="var(--yellow)" stroke-width="4"/>
    <polyline points="563,313 571,321 584,306" fill="none" stroke="var(--yellow)" stroke-width="5" stroke-linecap="round" stroke-linejoin="round"/>
    <!-- deploy: rocket -->
    <path d="M797 240 c-30 4 -52 30 -58 60 l16 16 c30 -6 56 -28 60 -58z" fill="var(--ink)"/>
    <circle cx="783" cy="272" r="8" fill="var(--orange)"/>
    <path d="M745 290 l-20 4 l14 -22 l18 -2z M764 309 l-4 20 l22 -14 l2 -18z" fill="var(--ink)"/>
    <path d="M736 310 l-14 22 l22 -14z" fill="var(--ink)"/>
    <!-- support: headset -->
    <circle cx="962" cy="268" r="24" fill="var(--ink)"/>
    <path d="M922 330 c4 -26 20 -34 40 -34 s36 8 40 34z" fill="var(--ink)"/>
    <path d="M930 272 a32 32 0 0 1 64 0" fill="none" stroke="var(--ink)" stroke-width="6"/>
    <rect x="924" y="262" width="12" height="22" rx="4" fill="var(--ink)"/><rect x="988" y="262" width="12" height="22" rx="4" fill="var(--ink)"/>
  </svg>
  <span class="stage-label" style="left:54px">Design</span>
  <span class="stage-label" style="left:262px">Develop</span>
  <span class="stage-label" style="left:469px">Test</span>
  <span class="stage-label" style="left:677px">Deploy</span>
  <span class="stage-label" style="left:882px">Support</span>
  <div class="footer-brand"><span class="dot"></span><span class="name">QUILMO<br>ENTERPRISES</span></div>
  <div class="page-no">05</div>
</section>

<!-- Closing -->
<section class="slide slide--brand" style="top:3428px">
  <h2 class="cover-title" style="top:66px;font-size:44px">Let Quilmo Help You</h2>
  <div class="lockup-mark" style="left:299px;top:214px"></div>
  <div class="lockup-name" style="left:511px;top:226px">QUILMO<br>ENTERPRISES</div>
  <h1 class="cover-title" style="top:432px">QUILMO ENTERPRISES</h1>
  <p class="cover-tagline" style="top:496px">Consolidate and Drive Your Buisness</p>
  <div class="page-no">06</div>
</section>

</body>
</html>
```